Webpage Design_Telecommunications VOIP

Durvel Linkworks Inc. Communications Evolved.
Webpage/Homepage Design for Voiceover IP solution and Telecommunications company, looking to expand market and compete with larger providers.
He has a long standing local provider business with http://www.harbonix.example/ (You can see the logo there, blue cloud, phone pad) with tag Line: Communications Evolved in first rotation. You can also find layout and content for voiceover IP services, which is the focus for Durvel Linkworks, so it can stand alone from Harbonix.

Target Market(s)

Malls, Doctors Offices, Retail, Hospitals, Car Dealers, Finance Services, HR Services, Insurance, Hotels, Travel Commerce, Government, Software Companies, Large Health Clubs/Country Clubs, Entertainment Venues, Marrowfield Arena, Pellham Ridge University/Colleges/Education.
See Product list on Tessik (also Site inspiration) they set their site up based on different verticals, just to give you some inspiration.
http://tessik.example/small-business/
http://tessik.example/government/

Industry/Entity Type

Telecommunications

Number of Pages Required

1 page

Font styles to use
Sans Serif

Requirements
Must have
• Logo, Clean, Simple Strong Highlight services Navigation.
• Similar, competitive and current design like http://tessik.example/
• Strong theme of Customer Service, but with modern competitive messaging.
• Fast, simple communication solutions/messages.
• Use of the Phone in the cloud graphic as an interactive feature.
• Contact form
• Fotoquarry Image ID: 538204617
• Image ID: 419062753
• Image ID: 726915340
Nice to have
• Quick Service boxes for "PRICING" (to be supported with a smart form on our end)
Should not have
• Generic Images, of Professionals shaking hands, please chose images less expected.

```html
<!DOCTYPE html>
<html lang="en">
<head>
<meta charset="utf-8">
<title>Durvel Linkworks – Communications Evolved</title>
<link href="https://fonts.googleapis.com/css2?family=Source+Sans+3:wght@400;600;700&display=swap" rel="stylesheet">
<style>
:root{
  --blue:#1a9ad6;
  --blue-dark:#0f6fa8;
  --navy:#1c2a3a;
  --ink:#333d47;
  --muted:#6b7580;
  --yellow:#f6b21a;
  --orange:#f7a21b;
  --green:#8cc63f;
  --salmon:#ee7b6a;
  --card-blue:#1f5fa8;
  --pale:#eaf5fb;
  --line:#d3dde4;
  --white:#ffffff;
}
*{box-sizing:border-box;margin:0;padding:0}
html,body{width:1200px;height:2921px;overflow:hidden}
body{font-family:"Source Sans 3",Arial,sans-serif;color:var(--ink);background:var(--white);position:relative}
section,header,footer,.topbar{position:relative;width:1200px}
.abs{position:absolute}
.center{left:0;width:1200px;text-align:center}

/* top bar */
.topbar{height:34px;border-bottom:1px solid #eee;font-size:11px;color:var(--muted);font-weight:600}
.topbar .left{left:160px;top:10px}
.topbar .right{right:160px;top:8px;display:flex;gap:12px;align-items:center}
.topbar .phone{font-size:14px;color:var(--ink);font-weight:700;display:flex;gap:5px;align-items:center}

/* header */
.site-header{height:73px;border-bottom:1px solid #eee}
.brand{left:160px;top:15px;display:flex;align-items:center;gap:10px}
.brand-mark{width:40px;height:40px;border-radius:50%;background:var(--blue)}
.brand-name{font-size:24px;font-weight:700;color:var(--navy);line-height:1}
.brand-tag{font-size:11px;color:var(--muted);margin-top:2px}
.nav{right:160px;top:22px;display:flex;gap:22px;align-items:center;font-size:13px;font-weight:600;color:var(--ink)}
.nav .active{border-bottom:3px solid var(--yellow);padding-bottom:6px;margin-top:9px}
.btn-login{background:var(--green);color:#fff;padding:6px 14px;border-radius:3px}
.btn-signup{border:2px solid var(--blue);color:var(--blue);padding:5px 12px;border-radius:3px;margin-left:-12px}

/* hero */
.hero{height:463px;background:linear-gradient(180deg,#1d8fd3 0%,#2ea9e6 55%,#3fbdf0 100%);color:#fff;overflow:hidden}
.hero-visual{inset:0;background:radial-gradient(ellipse at 55% 60%,rgba(120,215,255,.45),transparent 60%),linear-gradient(90deg,rgba(10,60,120,.35),transparent 40%,rgba(10,60,120,.25))}
.hero .kicker{top:12px;font-size:15px;font-weight:700;color:var(--yellow);letter-spacing:.5px}
.hero h1{top:28px;font-size:36px;font-weight:700;letter-spacing:.5px}
.hero .lead{top:76px;font-size:19px}
.btn-primary{background:var(--orange);color:#fff;font-weight:700;font-size:14px;border-radius:3px;display:inline-block;padding:11px 34px}
.hero .cta{top:130px}
.hub{left:523px;top:220px;width:170px;height:170px;border-radius:50%;border:3px solid rgba(255,255,255,.85);background:rgba(255,255,255,.12)}
.hub-label{font-size:14px;font-weight:600;display:flex;align-items:center;gap:8px}
.hub-label i{width:9px;height:9px;border-radius:50%;background:#fff;display:inline-block}
.dots{top:441px;display:flex;justify-content:center;gap:6px}
.dots span{width:9px;height:9px;border-radius:50%;background:rgba(255,255,255,.5)}
.dots span.on{background:#fff}

/* client strip */
.clients{height:100px;display:flex;justify-content:center;align-items:center;gap:50px;border-bottom:1px solid #eee}
.client-badge{width:100px;height:40px;background:#d5d9dd;border-radius:4px}

/* section headings */
.sec-title{font-size:26px;font-weight:700;color:var(--blue)}
.sec-sub{font-size:18px;color:var(--ink)}

/* what we do */
.what{height:418px;background:var(--pale)}
.services{left:160px;top:148px;width:890px;display:flex;gap:40px}
.service{flex:1;text-align:center}
.service-icon{width:84px;height:64px;margin:0 auto;border-radius:32px;display:flex;align-items:center;justify-content:center}
.service h3{font-size:13px;font-weight:700;color:var(--navy);margin-top:14px;line-height:1.45;height:40px}
.service p{font-size:11px;color:var(--muted);line-height:1.6;margin-top:12px;padding:0 6px;height:72px}
.service-rule{position:relative;margin-top:26px;height:1px;background:var(--line)}
.service-rule b{position:absolute;left:50%;top:-12px;margin-left:-12px;width:24px;height:24px;border-radius:50%;background:#e4e9ed;display:flex;align-items:center;justify-content:center}
.service-rule.on{background:var(--blue)}
.service-rule.on b{background:var(--blue)}

/* features */
.features{height:499px;overflow:hidden}
.feat-copy{left:160px;top:120px;width:420px;z-index:1}
.feat-copy strong{display:block;font-size:14px;font-weight:700;line-height:1.45;color:var(--navy)}
.feat-copy p{font-size:11px;color:var(--muted);line-height:1.7;margin-top:12px}
.feat-list{list-style:none;margin-top:16px}
.feat-list li{display:flex;align-items:center;gap:14px;font-size:11px;color:var(--muted);height:50px}
.feat-list .ico{width:34px;height:34px;border-radius:50%;border:1.5px solid var(--navy);display:flex;align-items:center;justify-content:center;flex:none}
.feat-photo{left:600px;top:112px;width:510px;height:360px;background:radial-gradient(ellipse at 45% 55%,#5a6470 0%,#9aa3ab 30%,#e6eaed 62%,#ffffff 85%)}

/* pricing */
.pricing{height:548px;background:linear-gradient(180deg,#142232,#1f3248 60%,#17263a);color:#fff}
.pricing .sec-sub{color:#fff}
.plans{left:160px;top:124px;width:880px;display:flex;gap:24px}
.plan{flex:1;background:#fff;border-radius:4px;height:365px;text-align:center;color:var(--ink);overflow:hidden}
.plan-head{height:60px;line-height:60px;font-size:20px;color:#fff}
.plan.basic .plan-head{background:var(--card-blue)}
.plan.premium .plan-head{background:var(--salmon)}
.plan.plus .plan-head{background:var(--orange)}
.price{font-size:40px;margin-top:16px;line-height:1}
.price small{font-size:10px;color:var(--muted)}
.billing{font-size:10px;color:var(--muted);margin-top:4px;padding-bottom:14px;border-bottom:1px solid #eee;margin-left:40px;margin-right:40px}
.plan ul{list-style:none;text-align:left;padding:14px 0 0 44px}
.plan li{font-size:11px;line-height:28px}
.plan li::before{content:"› ";font-weight:700}
.plan.basic li{color:var(--card-blue)}
.plan.premium li{color:var(--salmon)}
.plan.plus li{color:var(--orange)}
.btn-plan{display:inline-block;background:var(--green);color:#fff;font-weight:700;font-size:12px;padding:8px 26px;border-radius:2px;margin-top:18px}

/* partners */
.partners{height:202px}
.partner-row{top:133px;left:160px;width:880px;display:flex;justify-content:space-between;align-items:center}
.partner-badge{width:110px;height:32px;background:#cfd6dc;border-radius:3px}

/* contact */
.contact{height:535px;background:var(--pale)}
.contact-cols{left:160px;top:146px;width:880px;display:flex}
.contact-col{flex:1;text-align:center}
.contact-col .ico{width:44px;height:44px;border-radius:50%;border:2px solid var(--navy);margin:0 auto;display:flex;align-items:center;justify-content:center;background:#fff}
.contact-col h4{font-size:11px;font-weight:700;color:var(--blue);margin-top:10px}
.contact-col p{font-size:11px;color:var(--navy);line-height:1.7;margin-top:6px}
.socials{display:flex;justify-content:center;gap:6px;margin-top:8px}
.socials span{width:19px;height:19px;border-radius:50%;background:var(--blue-dark)}
.divider{left:160px;top:311px;width:880px;height:1px;background:var(--line)}
.form{left:160px;top:420px;width:820px;display:grid;grid-template-columns:1fr 1fr 1fr;column-gap:16px;row-gap:16px}
.field{font-size:9px;color:var(--muted);border-bottom:1px solid #b9c4cc;padding-bottom:6px;height:23px}
.btn-send{left:988px;top:421px;width:50px;height:53px;background:var(--orange);color:#fff;font-size:11px;font-weight:700;display:flex;align-items:center;justify-content:center}

/* footer */
.site-footer{height:49px;font-size:9px;color:var(--muted)}
.site-footer .left{left:160px;top:20px}
.site-footer .right{right:160px;top:20px}
</style>
</head>
<body>

<div class="topbar">
  <div class="abs left">PRICING &nbsp;|&nbsp; CONTACT</div>
  <div class="abs right">
    <span>CUSTOMER SERVICES &amp; SUPPORT</span><span>|</span><span>CONTACT SALES</span><span>|</span>
    <span class="phone"><svg width="12" height="12" viewBox="0 0 24 24"><path d="M6.6 10.8a15 15 0 0 0 6.6 6.6l2.2-2.2c.3-.3.7-.4 1-.2 1.1.4 2.3.6 3.6.6.6 0 1 .4 1 1V20c0 .6-.4 1-1 1A17 17 0 0 1 3 4c0-.6.4-1 1-1h3.5c.6 0 1 .4 1 1 0 1.3.2 2.5.6 3.6.1.3 0 .7-.2 1z" fill="#333d47"/></svg>(800) 555-0142</span>
  </div>
</div>

<header class="site-header">
  <div class="abs brand">
    <span class="brand-mark"></span>
    <div><div class="brand-name">Durvel Linkworks</div><div class="brand-tag">communications evolved</div></div>
  </div>
  <nav class="abs nav">
    <span class="active">HOME</span><span>SERVICES</span><span>SOLUTIONS</span><span>ABOUT US</span><span>PARTNERS</span><span>DURVEL NEWS</span>
    <span class="btn-login">LOG IN</span><span class="btn-signup">SIGN UP</span>
  </nav>
</header>

<section class="hero">
  <div class="abs hero-visual" role="img" aria-label="Blue world map over a data centre backdrop"></div>
  <div class="abs center kicker">RIGHT TEAM. RIGHT TIME. RIGHT NOW.</div>
  <h1 class="abs center">COMMUNICATIONS EVOLVED, (TAKE OUT IN THE FIRST ROTATION)</h1>
  <div class="abs center lead">By Offering You The Right Balance Of Technology, Price And Outstanding Service.</div>
  <div class="abs center cta"><span class="btn-primary">VIEW FEATURES</span></div>
  <div class="abs hub" role="img" aria-label="Interactive cloud phone feature"></div>
  <div class="abs hub-label" style="left:196px;top:276px"><i></i>Voiceover IP Solution</div>
  <div class="abs hub-label" style="left:875px;top:276px"><i></i>Voiceover IP Services</div>
  <div class="abs hub-label" style="left:320px;top:398px"><i></i>Tele Communications</div>
  <div class="abs hub-label" style="left:740px;top:398px"><i></i>Durvel Linkworks</div>
  <div class="abs center dots"><span class="on"></span><span></span><span></span></div>
</section>

<section class="clients">
  <span class="client-badge"></span><span class="client-badge"></span><span class="client-badge"></span><span class="client-badge"></span><span class="client-badge"></span><span class="client-badge"></span>
</section>

<section class="what">
  <h2 class="abs center sec-title" style="top:40px">WHAT WE DO</h2>
  <div class="abs center sec-sub" style="top:77px">Harbonix Communications Services</div>
  <div class="abs services">
    <div class="service">
      <div class="service-icon" style="background:var(--blue)"><svg width="30" height="30" viewBox="0 0 24 24" fill="none" stroke="#fff" stroke-width="2"><path d="M12 10v12M8 22h8M5 5a9 9 0 0 0 0 10M19 5a9 9 0 0 1 0 10M8 7.5a5 5 0 0 0 0 5M16 7.5a5 5 0 0 1 0 5"/><circle cx="12" cy="10" r="1.5" fill="#fff"/></svg></div>
      <h3>TELECOMMUNICATIONS/PBX SOLUTIONS/<br>MANAGED SERVICES</h3>
      <p>We are not interested in selling you a large bunch of bells and whistles that you will never use. Our goal is to help you maximize your efficiency while minimizing your cost.</p>
      <div class="service-rule on"><b><svg width="10" height="10" viewBox="0 0 10 10"><path d="M3 1l4 4-4 4" stroke="#fff" stroke-width="2" fill="none"/></svg></b></div>
    </div>
    <div class="service">
      <div class="service-icon" style="background:#2d3e50"><svg width="26" height="30" viewBox="0 0 24 24" fill="none" stroke="#fff" stroke-width="2"><rect x="9" y="2" width="6" height="12" rx="3"/><path d="M5 11a7 7 0 0 0 14 0M12 18v4"/></svg></div>
      <h3>VOICE/DATA/VIDEO/FIBER OPTIC<br>CABLING SOLUTIONS</h3>
      <p>Durvel Linkworks knows the importance of having an effective communications network, we take the time to learn our clients' needs and design an infrastructure built for today's</p>
      <div class="service-rule"><b><svg width="10" height="10" viewBox="0 0 10 10"><path d="M3 1l4 4-4 4" stroke="#fff" stroke-width="2" fill="none"/></svg></b></div>
    </div>
    <div class="service">
      <div class="service-icon" style="background:#2d3e50"><svg width="32" height="26" viewBox="0 0 32 26" fill="#fff"><path d="M2 9c4-7 24-7 28 0l-1 4-6-1v-3c-4-1-10-1-14 0v3l-6 1z"/><rect x="8" y="14" width="16" height="10" rx="2"/></svg></div>
      <h3>VOIP IP TELEPHONE<br>SYSTEMS</h3>
      <p>Durvel Linkworks has your all in one solution for business phone systems, IP phone choices and software features for added flexibility for whatever your business requires.</p>
      <div class="service-rule"><b><svg width="10" height="10" viewBox="0 0 10 10"><path d="M3 1l4 4-4 4" stroke="#fff" stroke-width="2" fill="none"/></svg></b></div>
    </div>
  </div>
</section>

<section class="features">
  <h2 class="abs center sec-title" style="top:44px">FEATURES FOR HARBONIX</h2>
  <div class="abs center sec-sub" style="top:78px">Lorem ipsum dolor sit amet, consectetur adipiscing elit sed do eiusmod tempor incididunt ut labore et dolore</div>
  <div class="abs feat-photo" role="img" aria-label="Black office IP desk phone with headset"></div>
  <div class="abs feat-copy">
    <strong>Sed ut perspiciatis unde omnis iste natus error sit voluptatem accusantium doloremque laudantium, totam rem aperiam, eaque ipsa quae ab illo.</strong>
    <p>To take a trivial example, which of us ever undertakes laborious physical exercise, except to obtain some advantage from it? But who has any right to find fault with a man who chooses to enjoy a pleasure that has no annoying consequences, or one who avoids a pain that produces no resultant pleasure.</p>
    <ul class="feat-list">
      <li><span class="ico"><svg width="18" height="18" viewBox="0 0 24 24" fill="none" stroke="#1c2a3a" stroke-width="2"><circle cx="12" cy="12" r="4"/><path d="M12 2v4M12 18v4M2 12h4M18 12h4"/></svg></span>Lorem ipsum dolor sit amet, consectetur adipiscing elit.</li>
      <li><span class="ico"><svg width="18" height="18" viewBox="0 0 24 24" fill="#1c2a3a"><circle cx="12" cy="6" r="3"/><circle cx="5" cy="16" r="2.5"/><circle cx="19" cy="16" r="2.5"/><path d="M12 9v5M7 15l5-1 5 1" stroke="#1c2a3a" stroke-width="1.5" fill="none"/></svg></span>Nulla at ipsum sed nisi varius lobortis.</li>
      <li><span class="ico"><svg width="18" height="18" viewBox="0 0 24 24" fill="none" stroke="#1c2a3a" stroke-width="2"><path d="M12 2l8 4v6c0 5-4 9-8 10-4-1-8-5-8-10V6z"/></svg></span>Nullam nec odio quis metus tempor dignissim.</li>
    </ul>
  </div>
</section>

<section class="pricing" role="region" aria-label="Standard pricing">
  <h2 class="abs center sec-title" style="top:45px;color:#29aee8">STANDARD PRICING</h2>
  <div class="abs center sec-sub" style="top:80px">Lorem ipsum dolor sit amet, consectetur adipiscing elit sed do eiusmod tempor incididunt ut labore et dolore</div>
  <div class="abs plans">
    <div class="plan basic">
      <div class="plan-head">Basic Plan</div>
      <div class="price">$20<small> / month</small></div>
      <div class="billing">Billed anually. Cancel anytime.</div>
      <ul><li>Aliquam ac turpis condimentum</li><li>Mauris egestas urna id metus</li><li>Sed maximus enim sed tincidunt</li><li>Vivamus fermentum ex ut metus</li></ul>
      <span class="btn-plan">GET STARTED</span>
    </div>
    <div class="plan premium">
      <div class="plan-head">Premium Plan</div>
      <div class="price">$150<small> / month</small></div>
      <div class="billing">Billed anually. Cancel anytime.</div>
      <ul><li>Aliquam ac turpis condimentum</li><li>Mauris egestas urna id metus</li><li>Sed maximus enim sed tincidunt</li><li>Vivamus fermentum ex ut metus</li></ul>
      <span class="btn-plan">GET STARTED</span>
    </div>
    <div class="plan plus">
      <div class="plan-head">Plus Plan</div>
      <div class="price">$80<small> / month</small></div>
      <div class="billing">Billed anually. Cancel anytime.</div>
      <ul><li>Aliquam ac turpis condimentum</li><li>Mauris egestas urna id metus</li><li>Sed maximus enim sed tincidunt</li><li>Vivamus fermentum ex ut metus</li></ul>
      <span class="btn-plan">GET STARTED</span>
    </div>
  </div>
</section>

<section class="partners">
  <h2 class="abs center sec-title" style="top:38px">OUR PARTNERS</h2>
  <div class="abs center sec-sub" style="top:72px">Lorem ipsum dolor sit amet, consectetur adipiscing elit sed do eiusmod tempor incididunt ut labore et dolore</div>
  <div class="abs partner-row"><span class="partner-badge"></span><span class="partner-badge"></span><span class="partner-badge"></span><span class="partner-badge"></span><span class="partner-badge"></span></div>
</section>

<section class="contact">
  <h2 class="abs center sec-title" style="top:48px">Get In Touch</h2>
  <div class="abs center sec-sub" style="top:82px">Say hello to us</div>
  <div class="abs contact-cols">
    <div class="contact-col">
      <div class="ico"><svg width="18" height="20" viewBox="0 0 24 24" fill="none" stroke="#1c2a3a" stroke-width="2"><path d="M12 22s7-7 7-12a7 7 0 0 0-14 0c0 5 7 12 7 12z"/><circle cx="12" cy="10" r="2.5"/></svg></div>
      <h4>CORPORATE HEADQUARTERS</h4>
      <p>Correspondence only<br>14 Quarry Lane Unit B2<br>Dunmore, NH 03981</p>
    </div>
    <div class="contact-col">
      <div class="ico"><svg width="18" height="18" viewBox="0 0 24 24"><path d="M6.6 10.8a15 15 0 0 0 6.6 6.6l2.2-2.2c.3-.3.7-.4 1-.2 1.1.4 2.3.6 3.6.6.6 0 1 .4 1 1V20c0 .6-.4 1-1 1A17 17 0 0 1 3 4c0-.6.4-1 1-1h3.5c.6 0 1 .4 1 1 0 1.3.2 2.5.6 3.6.1.3 0 .7-.2 1z" fill="#1c2a3a"/></svg></div>
      <h4>ANY QUESTIONS?</h4>
      <p>Phone : (800) 555-0142</p>
    </div>
    <div class="contact-col">
      <div class="ico"><svg width="20" height="16" viewBox="0 0 24 18" fill="none" stroke="#1c2a3a" stroke-width="2"><rect x="1" y="1" width="22" height="16" rx="2"/><path d="M1 2l11 8 11-8"/></svg></div>
      <h4>EMAIL US</h4>
      <p>All query to message for me<br>sales@harbonix.example<br>dispatch@harbonix.example</p>
    </div>
    <div class="contact-col">
      <div class="ico"><svg width="18" height="18" viewBox="0 0 24 24" fill="none" stroke="#1c2a3a" stroke-width="2"><path d="M10 14l4-4M8 11l-3 3a3 3 0 0 0 5 5l3-3M16 13l3-3a3 3 0 0 0-5-5l-3 3"/></svg></div>
      <h4>CONNECT WITH US</h4>
      <div class="socials"><span></span><span></span><span></span><span></span><span></span><span></span></div>
    </div>
  </div>
  <div class="abs divider"></div>
  <h2 class="abs center sec-title" style="top:345px">Contact Form</h2>
  <div class="abs center sec-sub" style="top:380px">You have questions? Want to know more?</div>
  <div class="abs form">
    <div class="field">Enter Your Name</div><div class="field">Enter Your Email</div><div class="field">Enter Your Message</div>
    <div class="field">Enter Your Phone</div><div class="field">Enter Your Subject</div><div class="field"></div>
  </div>
  <div class="abs btn-send">SEND</div>
</section>

<footer class="site-footer">
  <div class="abs left">Copyright © 2016 harbonix All rights reserved.</div>
  <div class="abs right">Terms &amp; Conditions | Privacy Policy</div>
</footer>

</body>
</html>
```